Home inspection business! professional look attracting customers just by looks. Read must haves

its a new business I started on my own for home inspections I would like something very professional to give to real estate agents and clients, its going to have my license number on it my business phone number my name my website as well etc on the back side it will be servicing areas and also what kind of services I offer I also have a business card from someone else the way I would like mine to be. I will attach my logo

Home Inspection

listed in nice to haves

• phone number - 555 293 8471
• website- hollowpinecheck.com
• license number #2938475610
• my name Gavin keropulis
• picture of my logo and me on the front
• on the back of the card. stating I am servicing All of New York and Long Island
• also services I will offer will be home inspection -mold inspection -lead inspection -radon inspection -Termite Inspection -Infared Scan.
• and also we provide inspections for single family homes condos co-ops town-homes
• and commercial property
• same colors as the logos and also if you recommend fonts to look like the logo not sure up to you

```html
<!DOCTYPE html>
<html lang="en">
<head>
<meta charset="UTF-8">
<title>Hollow Pine Check – Business Card</title>
<link rel="stylesheet" href="https://fonts.googleapis.com/css2?family=Montserrat:wght@600;700&family=Titillium+Web:wght@400;600&display=swap">
<style>
  :root {
    --page-bg: #e7e4df;
    --card-white: #f7f7f6;
    --brand-blue: #5b93cc;
    --edge-grey: #5c5d60;
    --ink-dark: #4a4b4e;
    --back-top: #6e6f72;
    --back-bottom: #4c4d50;
    --back-text: #f1f1f1;
  }
  * { margin: 0; padding: 0; box-sizing: border-box; }
  html, body { width: 1200px; height: 859px; overflow: hidden; background: var(--page-bg); }
  .canvas { position: relative; width: 1200px; height: 859px; }

  .card {
    position: absolute; top: 288px; width: 501px; height: 286px;
    overflow: hidden; box-shadow: 0 6px 14px rgba(0,0,0,.25);
  }

  /* Front */
  .card-front { left: 60px; background: var(--card-white); font-family: "Titillium Web", sans-serif; color: var(--ink-dark); }
  .front-shape { position: absolute; inset: 0; }
  .holder-name {
    position: absolute; left: 27px; top: 62px;
    font-family: "Montserrat", sans-serif; font-weight: 700; font-size: 19px;
    color: var(--brand-blue); text-transform: uppercase; letter-spacing: .2px;
  }
  .holder-role { position: absolute; left: 27px; top: 85px; font-size: 13px; }
  .front-rule { position: absolute; left: 27px; top: 118px; width: 202px; border-top: 1px solid var(--ink-dark); }
  .contact-list { position: absolute; left: 27px; top: 139px; list-style: none; font-size: 13px; line-height: 17.5px; }
  .contact-list li { display: flex; align-items: center; gap: 6px; }
  .contact-list svg { width: 13px; height: 13px; flex: none; }
  .accent { color: var(--brand-blue); font-weight: 600; }
  .license { position: absolute; left: 27px; top: 211px; font-size: 13px; }

  /* Back */
  .card-back {
    left: 639px; background: linear-gradient(180deg, var(--back-top), var(--back-bottom));
    font-family: "Titillium Web", sans-serif; color: var(--back-text); text-align: center;
  }
  .brand-lockup {
    position: absolute; left: 0; right: 0; top: 80px;
    display: flex; justify-content: center; align-items: center; gap: 9px;
  }
  .brand-dot { width: 14px; height: 14px; border-radius: 50%; background: var(--brand-blue); }
  .brand-name { font-weight: 600; font-size: 24px; color: var(--back-text); letter-spacing: 1px; text-transform: uppercase; }
  .service-area {
    position: absolute; left: 0; right: 0; top: 146px;
    font-family: "Montserrat", sans-serif; font-weight: 600; font-size: 12px;
    color: var(--brand-blue); letter-spacing: .6px; text-transform: uppercase;
  }
  .back-rule { position: absolute; left: 28px; right: 28px; top: 175px; border-top: 1px solid var(--brand-blue); }
  .service-list { position: absolute; left: 0; right: 0; top: 187px; font-size: 13px; line-height: 18.5px; }
  .sep { color: var(--brand-blue); padding: 0 3px; }
  .property-note { position: absolute; left: 24px; right: 24px; top: 236px; font-size: 13px; line-height: 18px; }
</style>
</head>
<body>
<main class="canvas">

  <section class="card card-front">
    <svg class="front-shape" viewBox="0 0 501 286" aria-hidden="true">
      <circle cx="445" cy="143" r="163" fill="var(--edge-grey)"/>
      <circle cx="449" cy="143" r="159" fill="var(--brand-blue)"/>
    </svg>
    <h1 class="holder-name">Gavin Keropulis</h1>
    <p class="holder-role">Training Specialist</p>
    <div class="front-rule"></div>
    <ul class="contact-list">
      <li>
        <svg viewBox="0 0 16 16"><circle cx="8" cy="8" r="7" fill="none" stroke="var(--brand-blue)" stroke-width="1.3"/><path d="M5.5 4.5l1.4 1.6-.8 1c.5 1 1.3 1.8 2.3 2.3l1-.8 1.6 1.4-.8 1.3C7.8 11 5 8.2 4.7 5.3z" fill="var(--brand-blue)"/></svg>
        555 293 8471
      </li>
      <li>
        <svg viewBox="0 0 16 16"><rect x="1.5" y="3.5" width="13" height="9" fill="none" stroke="var(--brand-blue)" stroke-width="1.3"/><path d="M1.5 3.5L8 9l6.5-5.5" fill="none" stroke="var(--brand-blue)" stroke-width="1.3"/></svg>
        gavin@hollowpinecheck.com
      </li>
      <li>
        <svg viewBox="0 0 16 16"><circle cx="8" cy="8" r="6.5" fill="none" stroke="var(--brand-blue)" stroke-width="1.3"/><ellipse cx="8" cy="8" rx="3" ry="6.5" fill="none" stroke="var(--brand-blue)" stroke-width="1.1"/><path d="M1.5 8h13M2.5 5h11M2.5 11h11" stroke="var(--brand-blue)" stroke-width="1"/></svg>
        <span>www.<span class="accent">hollowpinecheck</span>.com</span>
      </li>
    </ul>
    <p class="license">License Number <span class="accent">#2938475610</span></p>
  </section>

  <section class="card card-back">
    <div class="brand-lockup">
      <span class="brand-dot"></span>
      <span class="brand-name">Hollow Pine Check</span>
    </div>
    <p class="service-area">I am servicing all of New York and Long Island</p>
    <div class="back-rule"></div>
    <p class="service-list">
      Home inspection<span class="sep">|</span>Mold inspection<span class="sep">|</span>Lead inspection<br>
      Radon inspection<span class="sep">|</span>Termite Inspection<span class="sep">|</span>Infared Scan
    </p>
    <p class="property-note">We provide inspections for single family homes condos co-ops town-homes and Commercial property.</p>
  </section>

</main>
</body>
</html>
```